Web design for an intellectual property law practice

I need to design a simple landing page that may in the future expand to a full site. It should be very high tech focused.

Target Market(s)

Anyone seeking legal services

Industry/Entity Type

Legal

Number of Pages Required

2 page

Font styles to use
Other font styles liked:
• The same font as my logo

Colors
ec1f27

Requirements
Must have
• My logo (see attached).
Nice to have
• Open to ideas.

```html
<!DOCTYPE html>
<html lang="en">
<head>
<meta charset="utf-8">
<title>Daniel R. Hollis – Patent Lawyer</title>
<link href="https://fonts.googleapis.com/css2?family=Roboto:wght@300;400;500;700&display=swap" rel="stylesheet">
<style>
  :root {
    --brand-red: #ec1f27;
    --hero-taupe: #c8beb8;
    --hero-taupe-dark: #b7aca5;
    --panel-grey: #ebe9e7;
    --ink: #222222;
    --body-grey: #6b6b6b;
    --muted: #9a9a9a;
    --white: #ffffff;
    --footer: #333333;
    --canvas: #ffffff;
  }
  * { margin: 0; padding: 0; box-sizing: border-box; }
  html, body { width: 1200px; height: 1000px; overflow: hidden; background: var(--canvas); }
  body { font-family: "Roboto", Arial, sans-serif; color: var(--ink); position: relative; }

  .page {
    position: absolute; left: 424px; top: 72px; width: 352px; height: 856px;
    background: var(--white);
    box-shadow: 0 10px 60px rgba(0,0,0,0.14);
    overflow: hidden;
  }
  .abs { position: absolute; }

  /* hero */
  .hero { left: 0; top: 0; width: 352px; height: 204px; background: var(--hero-taupe); }
  .brand-mark {
    left: 38px; top: 0; width: 43px; height: 27px; background: var(--brand-red);
    color: var(--white); font-size: 4.4px; font-weight: 700; letter-spacing: .2px;
    display: flex; align-items: flex-end; justify-content: center; padding-bottom: 4px; text-transform: uppercase;
  }
  .nav { top: 13px; font-size: 5px; color: var(--ink); }
  .nav a { position: absolute; color: inherit; text-decoration: none; white-space: nowrap; }
  .nav .current::after { content: ""; position: absolute; left: -1px; right: -1px; top: 7px; height: 1px; background: var(--brand-red); }
  .portrait {
    left: 16px; top: 38px; width: 105px; height: 166px;
    background: linear-gradient(180deg, #a89e98 0%, #5d5652 45%, #2c2a2b 100%);
    border-radius: 40px 40px 0 0;
  }
  .hero-title { left: 146px; top: 67px; width: 170px; font-size: 12px; line-height: 14px; font-weight: 700; color: var(--white); }
  .hero-text { left: 146px; top: 105px; width: 140px; font-size: 5.6px; line-height: 7.6px; font-weight: 300; color: var(--white); }
  .hero-btn {
    left: 146px; top: 160px; width: 52px; height: 13px; border: 1px solid var(--brand-red);
    color: var(--white); font-size: 4.6px; font-weight: 500; letter-spacing: .5px;
    display: flex; align-items: center; justify-content: center;
  }

  /* shared section titles */
  .section-title {
    left: 0; width: 352px; display: flex; justify-content: center; align-items: center; gap: 4px;
    font-size: 7.6px; font-weight: 700; color: var(--ink);
  }
  .section-title::before { content: ""; width: 14px; height: 1px; background: var(--brand-red); }

  .small-copy { font-size: 3.9px; line-height: 5.7px; color: var(--body-grey); }

  /* about */
  .about-accent-left { left: 0; top: 270px; width: 26px; height: 71px; background: var(--brand-red); }
  .about-accent-right { left: 149px; top: 270px; width: 12px; height: 71px; background: var(--brand-red); }
  .about-photo { left: 26px; top: 252px; width: 123px; height: 101px; background: linear-gradient(135deg, #eef3f7 0%, #cfdbe4 60%, #b4c3cf 100%); }
  .quote { left: 22px; top: 363px; width: 132px; font-size: 8.4px; line-height: 10px; font-weight: 300; color: var(--ink); text-align: justify; }
  .quote-author { left: 22px; top: 407px; font-size: 4.2px; color: var(--ink); display: flex; align-items: center; gap: 4px; text-transform: uppercase; }
  .quote-author::before { content: ""; width: 8px; height: 1px; background: var(--brand-red); }
  .about-copy { left: 172px; top: 250px; width: 153px; text-align: justify; }
  .about-copy p + p { margin-top: 5.7px; }

  /* services */
  .services { left: 0; top: 426px; width: 352px; height: 147px; background: var(--panel-grey); }
  .service { top: 44px; width: 100px; }
  .service h3 { font-size: 5.2px; line-height: 6.4px; font-weight: 500; color: var(--ink); margin-bottom: 8px; }

  /* faq */
  .faq-sub { left: 0; width: 352px; top: 613px; text-align: center; font-size: 5.2px; color: var(--muted); }
  .video { left: 108px; top: 628px; width: 135px; height: 70px; background: linear-gradient(135deg, #f1f1f1 0%, #d9e4e6 50%, #4aa5ab 100%); }
  .video-bar { left: 0; top: 0; width: 135px; height: 11px; background: linear-gradient(180deg, #6a6a6a, rgba(120,120,120,0)); }
  .play { left: 58px; top: 29px; }

  /* contact */
  .contact { left: 0; top: 713px; width: 352px; height: 115px; background: var(--panel-grey); }
  .contact-lines { left: 0; top: 43px; width: 352px; text-align: center; font-size: 5.4px; line-height: 9.6px; color: var(--ink); }
  .footer { left: 0; top: 828px; width: 352px; height: 28px; background: var(--footer); }
</style>
</head>
<body>
<main class="page">

  <header class="abs hero">
    <div class="abs brand-mark">Hollis IP</div>
    <nav class="abs nav" style="left:0;width:352px;">
      <a class="current" style="left:117px;">About</a>
      <a style="left:160px;">Services</a>
      <a style="left:202px;">F.A.Q.</a>
      <a style="left:244px;">Contact</a>
      <a style="left:286px;">+1 416 555 0142</a>
    </nav>
    <div class="abs portrait" role="img" aria-label="Portrait photograph of the lawyer in a dark suit"></div>
    <h1 class="abs hero-title">Protect your intellectual property</h1>
    <p class="abs hero-text">Daniel R. Hollis is a patent lawyer with expertise in the acquisition, protection &amp; enforcement of intellectual property in Canada. Helping you with your Canadian IP rights.</p>
    <div class="abs hero-btn">CONTACT</div>
  </header>

  <section>
    <h2 class="abs section-title" style="top:225px;">About me</h2>
    <div class="abs about-accent-left"></div>
    <div class="abs about-accent-right"></div>
    <div class="abs about-photo" role="img" aria-label="Photograph of hands reviewing documents and charts at a desk"></div>
    <blockquote class="abs quote">“When creation is your business model, you need to protect it. Securing effective IP protection is the best way to do that!”</blockquote>
    <div class="abs quote-author">Daniel R. Hollis</div>
    <div class="abs about-copy small-copy">
      <p>DANIEL R. HOLLIS is a partner with Marrow Lane LLP in its Toronto Office. Daniel is an intellectual property lawyer with the firm's Technology and Intellectual Property practice groups. Daniel's practice focuses on all aspects of the acquisition, protection, enforcement and strategic use of a wide range of intellectual property assets in Canada and around the world.</p>
      <p>Daniel acts for a range of clients, from individual inventors, start-ups and other early stage companies to large multinational companies, and is actively involved in counselling clients and providing strategic advice in a variety of technology areas, including biotechnology, chemistry, energy (mining, oil and gas), social media, insurance, communications and digital marketing. While focusing on biotechnology and other life sciences, “... his deep knowledge base enables him to handle matters across a range of disciplines with aplomb” (Patent Counsel Review, 2012).</p>
      <p>Daniel speaks and writes extensively on all aspects of intellectual property rights, particularly the commercialization of IP rights for start-ups as well as commercial matters for companies with respect to IP rights in national, cross-border and multinational commercial transactions. Daniel has been sought after by national and international media as a commentator on IP matters.</p>
    </div>
  </section>

  <section class="abs services">
    <h2 class="abs section-title" style="top:13px;">Services</h2>
    <div class="abs service" style="left:18px;">
      <h3>Patents &amp; Industrial Designs</h3>
      <p class="small-copy">As a registered patent agent with the Canadian Intellectual Property Office (CIPO), Daniel's practice focuses on the drafting and prosecuting of patent applications in Canada and throughout the world covering a range of subject matters, including biotechnology, chemistry and other life sciences. Daniel advises clients on patent protection strategies and how to proceed when faced with allegations of patent infringement. Daniel "... spearheads prosecution and monetisation initiatives for an impressive variety of companies."</p>
    </div>
    <div class="abs service" style="left:125px;">
      <h3>Trademark Protection</h3>
      <p class="small-copy">As a registered trademark agent, Daniel advises local, national and international clients on how to efficiently and effectively conduct branding strategies as well as protect, maintain and enforce trademark rights in Canada, the United States and other jurisdictions.</p>
    </div>
    <div class="abs service" style="left:235px;">
      <h3>Commercial Intellectual Property &amp; Commercialization of IP</h3>
      <p class="small-copy">Daniel is frequently called upon to advise clients on commercializing intellectual property rights, including technology acquisition and licensing, freedom to operate and patentability opinions, as well as IP components of high value national, cross-border and multi-jurisdictional corporate transactions (e.g. financing, mergers and acquisitions and joint ventures).</p>
    </div>
  </section>

  <section>
    <h2 class="abs section-title" style="top:592px;">F.A.Q.</h2>
    <p class="abs faq-sub">Why IP Matters to Your StartUp</p>
    <div class="abs video" role="img" aria-label="Video thumbnail with an illustrated diagram of IP types">
      <div class="abs video-bar"></div>
      <svg class="abs play" width="18" height="12" viewBox="0 0 18 12" aria-hidden="true">
        <rect width="18" height="12" rx="3" fill="#222"/>
        <path d="M7 3.5 L12 6 L7 8.5 Z" fill="#fff"/>
      </svg>
    </div>
  </section>

  <section class="abs contact">
    <h2 class="abs section-title" style="top:20px;">Contact</h2>
    <div class="abs contact-lines">
      Questions?<br>Don't hesitate to reach out if you have any questions<br><br>Canadian Patent Lawyer<br>+1 416 555 0142
    </div>
  </section>

  <footer class="abs footer"></footer>
</main>
</body>
</html>
```